Envelope Design - Winner can do follow-up business

- Marvuno.com is a Swiss-based online store selling business shirts and accessories for business men
- Please visit the webpage to make yourself familiar with the company. Although the text is in German, with Google translator you should be able to understand the main content.
- Our clients are mainly business men between 30 and 60 years old. Mostly with a high income working in the service industry (banking, insurance, lawyers, etc.). Sometimes there wives purchase the shirts for them ;-)
- The colors and the logo are given, as they are also used for the print materials (please see files in attachment)
- I am running several businesses and often need a talented web designer --> the winner gets substantial follow-up business
your task:
-for our company we need a new envelope design
-It should be simple and modern
-please use one of the logos in the followings.
-suprise me :)

```html
<!DOCTYPE html>
<html lang="en">
<head>
<meta charset="utf-8">
<title>Marvuno Envelope</title>
<link href="https://fonts.googleapis.com/css2?family=Lato:wght@400&display=swap" rel="stylesheet">
<style>
  :root {
    --backdrop: #e4e4e4;
    --paper: #ffffff;
    --gold: #e8d66c;
    --red: #ee3124;
    --black: #000000;
    --label: #ffffff;
  }
  html, body {
    margin: 0;
    padding: 0;
    width: 1200px;
    height: 810px;
    overflow: hidden;
    background: var(--backdrop);
  }
  .envelope {
    position: absolute;
    left: 46px;
    top: 164px;
    width: 1107px;
    height: 482px;
    background: var(--paper);
  }
  .band {
    position: absolute;
  }
  .band--gold-side   { left: 0; top: 0; width: 16px; height: 482px; background: var(--gold); }
  .band--gold-bottom { left: 0; bottom: 0; width: 1107px; height: 16px; background: var(--gold); }
  .band--red-side    { left: 16px; top: 0; width: 16px; height: 466px; background: var(--red); }
  .band--red-bottom  { left: 16px; bottom: 16px; width: 1091px; height: 16px; background: var(--red); }
  .brand-block {
    position: absolute;
    left: 32px;
    top: 272px;
    width: 179px;
    height: 178px;
    background: var(--black);
    display: flex;
    align-items: center;
    justify-content: center;
  }
  .brand-name {
    font-family: "Lato", sans-serif;
    font-size: 20px;
    font-weight: 400;
    letter-spacing: 0;
    color: var(--label);
  }
</style>
</head>
<body>
  <div class="envelope">
    <div class="band band--gold-side"></div>
    <div class="band band--gold-bottom"></div>
    <div class="band band--red-side"></div>
    <div class="band band--red-bottom"></div>
    <div class="brand-block">
      <span class="brand-name">Marvuno</span>
    </div>
  </div>
</body>
</html>
```